Business Card Design Project

We need a logo design for a new company based in Southern California called "Norvale Security Services, Inc." We install security and camera systems for homeowners and business, to protect their assets.
Updates

Project Deadline Extended
Reason: LOGO Design completes in eight days. Would like that design decided before we finish the business cards. Thanks...

Target Market(s)

Homeowners and business owners looking for additional protection of their assets.

Industry/Entity Type

Security

Font styles to use
Serif

Requirements
Must have
• Company Name
Office# 909-472-3615
Service# 909-472-3616
email: NorvaleSecurity@brimwell.net
address: 48620 Thorncrest Lane Rancho Cucamonga, CA 91704
Nice to have
• Serving Southern California

```html
<!DOCTYPE html>
<html lang="en">
<head>
<meta charset="utf-8">
<title>Norvale Security Services, Inc. — Business Card</title>
<link rel="stylesheet" href="https://fonts.googleapis.com/css2?family=Cormorant+SC:wght@500&family=Cormorant+Garamond:wght@500&display=swap">
<style>
  :root {
    --backdrop: #2a2a2a;
    --card-black: #050708;
    --pattern-teal: #1b4a5c;
    --pattern-deep: #0c2530;
    --ink-white: #f2f2f0;
  }
  html, body {
    margin: 0;
    width: 1200px;
    height: 869px;
    overflow: hidden;
    background: var(--backdrop);
  }
  .business-card {
    position: absolute;
    left: 75px;
    top: 134px;
    width: 1050px;
    height: 600px;
    background: var(--card-black);
    overflow: hidden;
    box-shadow: 0 10px 30px rgba(0,0,0,0.5);
  }
  .card-pattern {
    position: absolute;
    inset: 0;
    width: 100%;
    height: 100%;
  }
  .brand {
    position: absolute;
    left: 60px;
    top: 90px;
    display: flex;
    align-items: center;
    gap: 28px;
  }
  .brand-circle {
    width: 96px;
    height: 96px;
    border: 5px solid var(--ink-white);
    border-radius: 50%;
    box-sizing: border-box;
  }
  .brand-name {
    font-family: "Cormorant SC", serif;
    font-weight: 500;
    font-size: 40px;
    letter-spacing: 1.5px;
    color: var(--ink-white);
    margin: 0;
  }
  .contact-list {
    position: absolute;
    left: 75px;
    top: 330px;
    margin: 0;
    padding: 0;
    list-style: none;
    font-family: "Cormorant Garamond", serif;
    font-weight: 500;
    font-size: 24px;
    line-height: 38px;
    color: var(--ink-white);
  }
  .service-area {
    position: absolute;
    left: 75px;
    top: 500px;
    margin: 0;
    font-family: "Cormorant Garamond", serif;
    font-weight: 500;
    font-size: 24px;
    color: var(--ink-white);
  }
</style>
</head>
<body>
  <div class="business-card">
    <svg class="card-pattern" viewBox="0 0 1050 600" preserveAspectRatio="none" role="img" aria-label="Ornate teal lace medallion pattern on black covering the card">
      <defs>
        <radialGradient id="patternTone" cx="55%" cy="45%" r="75%">
          <stop offset="0%" stop-color="var(--pattern-teal)"/>
          <stop offset="60%" stop-color="var(--pattern-deep)"/>
          <stop offset="100%" stop-color="var(--card-black)"/>
        </radialGradient>
      </defs>
      <rect width="1050" height="600" fill="url(#patternTone)"/>
    </svg>

    <div class="brand">
      <div class="brand-circle"></div>
      <h1 class="brand-name">Norvale Security Services, Inc</h1>
    </div>

    <ul class="contact-list">
      <li>Office number: 909-472-3615</li>
      <li>Service number: 909-472-3616</li>
      <li>E-mail: NorvaleSecurity@brimwell.net</li>
      <li>Address: 48620 Thorncrest Lane Rancho Cucamonga, CA 91704</li>
    </ul>

    <p class="service-area">Serving Southern California</p>
  </div>
</body>
</html>
```